Rack card for a integrative medical practice

Need an eye-catching rack card with our logo with content as provided. We have a membership based holistic medical practice which incorporates western and holistic medicine. We would like to focus on wellness and healthy lifestyle. See uploaded files for what is included in the membership. Would like 2 page rack card color on both sides. Logo must be on the front.

Target Market(s)

People looking for alternative medicine, healthy lifestyle.

Industry/Entity Type

Health and Wellness

Colors
00AB8E
00BBA5
67D7C9
C6EFE9
E9F9F6

Requirements
Must have
• Must spark interest at first sight. Clear message.
Nice to have
• Warm, bright and positive vibe. Organic, neutral and earthy colors.
Should not have
• Traditional medical practice vibe (cold, formal, industrial). No PINK except the logo.

```html
<!DOCTYPE html>
<html lang="en">
<head>
<meta charset="utf-8">
<title>Alder Health &amp; Wellness – Rack Card</title>
<link rel="stylesheet" href="https://fonts.googleapis.com/css2?family=Poppins:wght@400;500;600&display=swap">
<style>
  :root {
    --stage: #555455;
    --maroon: #7a2a22;
    --maroon-light: #a24f38;
    --copper: #e09a62;
    --gold: #f0a54a;
    --white: #ffffff;
    --ink: #1d1d1d;
    --brand-green: #1f3a34;
  }
  * { margin: 0; padding: 0; box-sizing: border-box; }
  html, body {
    width: 813px; height: 1200px; overflow: hidden;
    background: var(--stage);
    font-family: "Poppins", sans-serif;
  }
  .canvas { position: relative; width: 813px; height: 1200px; }
  .card {
    position: absolute; top: 195px; width: 360px; height: 810px;
    overflow: hidden; background: var(--white);
    box-shadow: 0 10px 24px rgba(0,0,0,.35);
  }
  .card--front { left: 30px; }
  .card--back { left: 423px; background: var(--maroon); }

  /* front */
  .front-art { position: absolute; inset: 0; }
  .front-headline {
    position: absolute; left: 43px; top: 25px; width: 300px;
    color: var(--white); font-weight: 600; font-size: 21px; line-height: 28px;
  }
  .brand {
    position: absolute; left: 0; right: 0; text-align: center;
    color: var(--brand-green); font-weight: 500;
  }
  .front-brand { top: 605px; }
  .brand-mark {
    display: inline-block; width: 24px; height: 24px; border-radius: 50%;
    background: var(--copper); margin-bottom: 8px;
  }
  .brand-name { display: block; font-size: 40px; letter-spacing: 9px; line-height: 44px; padding-left: 9px; }
  .brand-tagline { display: block; font-size: 10px; letter-spacing: 4px; line-height: 14px; padding-left: 4px; }
  .front-rule {
    position: absolute; left: 43px; right: 43px; top: 733px;
    height: 2px; background: var(--gold);
  }
  .front-address {
    position: absolute; left: 0; right: 0; top: 748px; text-align: center;
    color: var(--ink); font-size: 14px; line-height: 20px;
  }

  /* back */
  .back-heading {
    position: absolute; left: 10px; right: 10px; top: 30px; text-align: center;
    color: var(--gold); font-weight: 600; font-size: 20px; line-height: 28px;
  }
  .benefits { list-style: none; position: absolute; left: 26px; right: 10px; top: 120px; }
  .benefit { display: flex; align-items: center; margin-bottom: 17px; }
  .benefit-number {
    flex: 0 0 36px; color: var(--white); font-weight: 600; font-size: 17px;
  }
  .benefit-text {
    border-left: 2px solid var(--gold); padding-left: 15px;
    color: var(--white); font-size: 15px; line-height: 20px; white-space: nowrap;
  }
  .back-footer {
    position: absolute; left: 0; right: 0; bottom: 0; height: 133px; background: var(--white);
  }
  .back-bar {
    position: absolute; left: 28px; right: 28px; top: -5px; height: 5px;
    background: var(--copper); border-radius: 3px 3px 0 0;
  }
  .back-brand { top: 26px; }
  .back-brand .brand-mark { width: 16px; height: 16px; margin-bottom: 4px; }
  .back-brand .brand-name { font-size: 24px; letter-spacing: 5px; line-height: 28px; padding-left: 5px; }
  .back-brand .brand-tagline { font-size: 6px; letter-spacing: 2.4px; line-height: 9px; }
</style>
</head>
<body>
<main class="canvas">

  <section class="card card--front">
    <svg class="front-art" width="360" height="810" viewBox="0 0 360 810">
      <defs>
        <linearGradient id="maroonFade" x1="0" y1="0" x2="0" y2="1">
          <stop offset="0" stop-color="#7a2a22"/>
          <stop offset="0.45" stop-color="#8a3527"/>
          <stop offset="1" stop-color="#a5503a"/>
        </linearGradient>
        <linearGradient id="photoTone" x1="0" y1="0" x2="1" y2="1">
          <stop offset="0" stop-color="#7d6148"/>
          <stop offset="0.55" stop-color="#9c8064"/>
          <stop offset="1" stop-color="#5e4536"/>
        </linearGradient>
      </defs>
      <rect class="front-band" width="360" height="600" fill="url(#maroonFade)"/>
      <path class="copper-arc" d="M0,322 C8,220 130,166 360,164 L360,172 C140,174 10,228 0,330 Z" fill="#e09a62"/>
      <path class="photo-area" role="img" aria-label="Photo of a woman meditating cross-legged on a mat beside a potted palm and candles"
            d="M0,330 C10,228 140,174 360,172 L360,395 C330,520 230,568 0,568 Z" fill="url(#photoTone)"/>
      <path class="front-white" d="M0,576 C240,576 335,525 360,405 L360,810 L0,810 Z" fill="#ffffff"/>
      <path class="copper-arc" d="M0,568 C230,568 330,520 360,395 L360,405 C335,525 240,576 0,576 Z" fill="#e09a62"/>
    </svg>
    <h1 class="front-headline">A direct primary care<br>practice Focused on a<br>moreholistic And<br>personal approach to<br>Medicine.</h1>
    <div class="brand front-brand">
      <span class="brand-mark"></span>
      <span class="brand-name">ALDER</span>
      <span class="brand-tagline">HEALTH &amp; WELLNESS</span>
    </div>
    <div class="front-rule"></div>
    <p class="front-address">1420 W Elm St., STE 2B<br>Riverton.</p>
  </section>

  <section class="card card--back">
    <h2 class="back-heading">WHAT'S INCLUDED IN YOUR<br>MEMBERSHIP</h2>
    <ol class="benefits">
      <li class="benefit"><span class="benefit-number">01</span><span class="benefit-text">Unlimited office visits with no<br>copay</span></li>
      <li class="benefit"><span class="benefit-number">02</span><span class="benefit-text">Direct communication with<br>your doctor</span></li>
      <li class="benefit"><span class="benefit-number">03</span><span class="benefit-text">Discounted labs, imaging and<br>medications</span></li>
      <li class="benefit"><span class="benefit-number">04</span><span class="benefit-text">Free initial acupuncture<br>session ($250 value)</span></li>
      <li class="benefit"><span class="benefit-number">05</span><span class="benefit-text">2 Bodymap testings per year<br>($100 value)</span></li>
      <li class="benefit"><span class="benefit-number">06</span><span class="benefit-text">Discounts for supplements<br>and health products in the<br>clinic</span></li>
      <li class="benefit"><span class="benefit-number">07</span><span class="benefit-text">Discounts for iv vitamin<br>infusion therapy</span></li>
      <li class="benefit"><span class="benefit-number">08</span><span class="benefit-text">Personalized nutrition plan<br>after advanced testing such<br>as gut microbiome, hormonal,<br>metabolism test, etc.</span></li>
    </ol>
    <div class="back-footer">
      <div class="back-bar"></div>
      <div class="brand back-brand">
        <span class="brand-mark"></span>
        <span class="brand-name">ALDER</span>
        <span class="brand-tagline">HEALTH &amp; WELLNESS</span>
      </div>
    </div>
  </section>

</main>
</body>
</html>
```